Spa Business Card Design Project

Hello! We are a boutique spa for men and women that is rebranding. I would like a memorable new business card that showcases our beautiful new logo and our unique business. I would like it to be classic/timeless and eclectic/artistic at the  same time.
I am a fan of negative space as you can tell from the logo. I am also open to any creative ideas.
Multi sided design. Two sided design is acceptable as an option, too. "Flaps/folds/whatever the design term is" are optional- whether full vertical or horizontal, half flap, full flap etc
On either side next to the golden snail I would potentially like to see "slow down. Enjoy Life."  Possibly on one statment on top of each other, crowned with the snail. Or the statment following the snail on one line... I am open for a creative suprise, too.
The back I would like room for the standard Information
"3817 Birch Lane
Ashbrook, New York 12731
(518) 462 3085
info@thecorvella spa.com
The snail is to be done in gold ink.
Can I also Have an option for cards that are individualized for staff members, too?

Updates
Project Deadline Extended
Reason: I apologize for the deadline extension. My day was more involved than anticipated in other matters. Hope to have this closed by next Tuesday.
Thank you

Target Market(s)
Men and women with expendable income between the ages of 30-55
Industry/Entity Type
Boutique
Requirements
Must have
- only black and gold ink.

Nice to have
- One of a kind.
Showcase the snail :-)
make you smile :-)
Fun, but professional.
Should not have
- Lots of color.
Too feminine.
Too busy.

```html
<!DOCTYPE html>
<html lang="en">
<head>
<meta charset="utf-8">
<title>The Corvella Spa – Business Cards</title>
<link rel="stylesheet" href="https://fonts.googleapis.com/css2?family=Mulish:wght@400;700&display=swap">
<style>
  :root {
    --backdrop: #3a4544;
    --backdrop-edge: #1f2626;
    --card: #141818;
    --card-front: #181b1b;
    --gold: #c9a24a;
    --gold-band: #b8923f;
    --faint-mark: #0c0e0e;
  }
  * { margin: 0; padding: 0; box-sizing: border-box; }
  html, body {
    width: 1200px;
    height: 886px;
    overflow: hidden;
  }
  body {
    position: relative;
    background: radial-gradient(ellipse at 50% 40%, var(--backdrop) 0%, var(--backdrop-edge) 100%);
    font-family: "Mulish", sans-serif;
    color: var(--gold);
  }
  .card {
    position: absolute;
    width: 555px;
    height: 317px;
    background: var(--card);
    box-shadow: 0 6px 18px rgba(0, 0, 0, 0.45);
  }
  .card--front { left: 29px; top: 85px; background: var(--card-front); }
  .card--back { left: 611px; top: 85px; }
  .card--staff { left: 325px; top: 459px; width: 553px; }

  .pattern-band {
    position: absolute;
    left: 0;
    width: 100%;
    height: 13px;
    background: var(--gold-band);
  }
  .pattern-band--top { top: 14px; }
  .pattern-band--bottom { top: 280px; }

  .brand {
    position: absolute;
    left: 0;
    width: 100%;
    top: 118px;
    text-align: center;
  }
  .brand__name {
    font-weight: 400;
    font-size: 34px;
    letter-spacing: 3px;
    text-transform: uppercase;
    color: var(--gold);
    white-space: nowrap;
  }
  .brand__tagline {
    margin-top: 12px;
    font-size: 12px;
    letter-spacing: 0.3px;
  }
  .motto {
    position: absolute;
    right: 23px;
    bottom: 21px;
    font-size: 13px;
    letter-spacing: 0.3px;
  }

  .contact {
    position: absolute;
    left: 0;
    width: 100%;
    top: 124px;
    text-align: center;
    font-style: normal;
    font-weight: 700;
    font-size: 11.5px;
    line-height: 14px;
  }
  .contact__item { display: block; white-space: nowrap; }

  .staff {
    position: absolute;
    left: 99px;
    top: 128px;
  }
  .staff__name {
    font-size: 25px;
    letter-spacing: 0.5px;
    text-transform: uppercase;
    line-height: 1;
    white-space: nowrap;
  }
  .staff__first { font-weight: 700; }
  .staff__last { font-weight: 400; }
  .staff__role {
    margin-top: 4px;
    font-size: 12.5px;
  }
  .staff-mark {
    position: absolute;
    left: 340px;
    top: 143px;
    font-size: 14px;
    letter-spacing: 1px;
    text-transform: uppercase;
    white-space: nowrap;
    color: var(--faint-mark);
  }
</style>
</head>
<body>

  <section class="card card--front">
    <div class="brand">
      <div class="brand__name">The Corvella Spa</div>
      <div class="brand__tagline">a boutique spa for Men &amp; Women</div>
    </div>
    <div class="motto">Slow down. Enjoy Life</div>
  </section>

  <section class="card card--back">
    <div class="pattern-band pattern-band--top" role="img" aria-label="Gold border of repeating snail ornaments"></div>
    <address class="contact">
      <span class="contact__item">(518) 462 3085</span>
      <span class="contact__item">info@thecorvella spa.com</span>
      <span class="contact__item">3817 Birch Lane ,Ashbrook, New York 12731</span>
    </address>
    <div class="pattern-band pattern-band--bottom" role="img" aria-label="Gold border of repeating snail ornaments"></div>
  </section>

  <section class="card card--staff">
    <div class="pattern-band pattern-band--top" role="img" aria-label="Gold border of repeating snail ornaments"></div>
    <div class="staff">
      <div class="staff__name"><span class="staff__first">Mirela</span><span class="staff__last">Dobreva</span></div>
      <div class="staff__role">occupation</div>
    </div>
    <div class="staff-mark">The Corvella Spa</div>
    <div class="pattern-band pattern-band--bottom" role="img" aria-label="Gold border of repeating snail ornaments"></div>
  </section>

</body>
</html>
```